Signage for a store*

logo on the two sides of the sign
in the middle is the name of the store witch is VORELT
at the bottom of the two logos, one side for location/address and the other side is contact details phone number is 718-392-6107 address is 2974 THE SIGN WILL BEE 15 FEET BY 4 FEET I WOULD LIKE THAT THE
BACKGROUND OF THE SIGN SHOULD HAVE A NICE COLOR BASE
THAT GOES FOR A WINE STORE

```html
<!DOCTYPE html>
<html lang="en">
<head>
<meta charset="utf-8">
<title>VORELT – Store Sign</title>
<link href="https://fonts.googleapis.com/css2?family=Courier+Prime:wght@400;700&display=swap" rel="stylesheet">
<style>
  :root {
    --sign-yellow: #f5d23c;
    --sign-glow: #fffbe6;
    --wine: #9e2a4a;
    --ink: #141414;
    --border-gold: #e8c22e;
    --wood: #c9a57a;
    --wood-dark: #8e6a45;
    --carton: #f1ece4;
    --carton-red: #c8343f;
  }
  html, body {
    margin: 0;
    padding: 0;
    width: 1200px;
    height: 320px;
    overflow: hidden;
    background: var(--sign-yellow);
  }
  .sign {
    position: relative;
    width: 1200px;
    height: 320px;
    overflow: hidden;
    background: radial-gradient(ellipse 300px 190px at 598px 158px, var(--sign-glow) 0%, #fbe89a 45%, var(--sign-yellow) 100%);
    font-family: "Courier Prime", "Courier New", monospace;
  }
  .border-band {
    position: absolute;
    left: 0;
    width: 1200px;
    background: linear-gradient(to bottom, var(--border-gold), #efcb3a);
  }
  .border-band--top { top: 0; height: 21px; }
  .border-band--bottom { bottom: 0; height: 26px; }

  .brand-mark {
    position: absolute;
    top: 58px;
    width: 140px;
    text-align: center;
    color: var(--wine);
    font-size: 26px;
    font-weight: 400;
    line-height: 1;
  }
  .brand-mark__dot {
    display: block;
    width: 30px;
    height: 30px;
    margin: 0 auto 10px;
    border-radius: 50%;
    background: var(--wine);
  }
  .brand-mark--left { left: 76px; }
  .brand-mark--right { left: 983px; }

  .address {
    position: absolute;
    left: 26px;
    top: 170px;
    width: 240px;
    margin: 0;
    text-align: center;
    color: var(--ink);
    font-size: 24px;
    line-height: 26px;
    font-style: normal;
  }

  .store-name {
    position: absolute;
    left: 0;
    top: 62px;
    width: 1196px;
    margin: 0;
    text-align: center;
    color: var(--wine);
    font-size: 160px;
    font-weight: 400;
    line-height: 1;
    letter-spacing: 8px;
  }

  .phone {
    position: absolute;
    left: 932px;
    top: 156px;
    width: 242px;
    text-align: center;
    color: var(--ink);
    font-size: 25px;
    line-height: 30px;
    font-weight: 700;
  }

  .product {
    position: absolute;
    top: 194px;
  }
  .product--wood-case {
    left: 964px;
    width: 95px;
    height: 114px;
    background: linear-gradient(135deg, var(--wood), var(--wood-dark));
  }
  .product--wine-carton {
    left: 1084px;
    width: 64px;
    height: 106px;
    background: linear-gradient(160deg, var(--carton) 55%, var(--carton-red));
  }
</style>
</head>
<body>
  <div class="sign">
    <div class="border-band border-band--top" role="img" aria-label="Gold ornamental border pattern"></div>

    <div class="brand-mark brand-mark--left"><span class="brand-mark__dot"></span>VORELT</div>

    <address class="address">VORELT<br>2974, Harlow St<br>Fenwick,<br>N.Y.10588</address>

    <h1 class="store-name">VORELT</h1>

    <div class="brand-mark brand-mark--right"><span class="brand-mark__dot"></span>VORELT</div>

    <div class="phone">718-392-6107</div>

    <div class="product product--wood-case" role="img" aria-label="Wooden gift case holding three wine bottles"></div>
    <div class="product product--wine-carton" role="img" aria-label="Boxed wine carton"></div>

    <div class="border-band border-band--bottom" role="img" aria-label="Gold ornamental border pattern"></div>
  </div>
</body>
</html>
```